Flyer for Luxury Boarding Stable for Retired Horses

A one page flyer to hand out at stable tours and at horse shows. Willow Brook at 34 Meadows is a luxury equine boarding stable for retired horses. This is a new facility in Cedar Hollow, TN that has 6 available stalls. We are trying to attract owners with 2 or more retired horses they would like to board.

Target Market(s)

Horse owners with 2 or more horses that are retired from showing, racing, or rodeo. These owners love their horses like family and want them well cared for in their retirement years.

Industry/Entity Type

Equestrian Boarding

Font styles to use
Script

Colors
EE7325
F08F49
F5BC92
FAE3D3
FDF4ED

Requirements
Must have
• Photos of the facility. Must feel upscale and worth the price.

```html
<!DOCTYPE html>
<html lang="en">
<head>
<meta charset="utf-8">
<title>Willow Brook at 34 Meadows — Retirement Horse Boarding</title>
<link href="https://fonts.googleapis.com/css2?family=Montserrat:wght@500;600&family=Cormorant+Garamond:ital,wght@1,500&family=Cutive&display=swap" rel="stylesheet">
<style>
  :root{
    --orange-deep:#EE7325;
    --orange:#F08F49;
    --orange-soft:#F5BC92;
    --peach:#FAE3D3;
    --cream:#FDF4ED;
    --ink:#1f1f1f;
    --page:#e9e9e9;
    --meadow-1:#5f8a2c;
    --meadow-2:#a9c15a;
    --meadow-3:#2f3b1c;
  }
  *{margin:0;padding:0;box-sizing:border-box}
  html,body{width:933px;height:1200px;overflow:hidden;background:var(--page)}
  .flyer{
    position:absolute;left:42px;top:0;width:836px;height:1183px;
    transform:scale(1.0144);transform-origin:top left;
    background:#fff;overflow:hidden;
  }
  .flyer-art{position:absolute;inset:0;width:836px;height:1183px}
  .title{
    position:absolute;left:50px;top:38px;
    font-family:"Montserrat",sans-serif;font-weight:600;font-size:28px;line-height:41px;color:#fff;
  }
  .facility-photo{
    position:absolute;left:45px;width:234px;height:234px;border-radius:50%;
    border:8px solid var(--orange);
  }
  .facility-photo.barn-aerial{top:466px;background:radial-gradient(circle at 55% 50%,#8c7b62 0,#b9b4a6 35%,#4f7a2c 75%)}
  .facility-photo.stall-aisle{top:698px;background:radial-gradient(circle at 50% 45%,#e8dcc0 0,#9a7147 40%,#6a4a2c 80%)}
  .facility-photo.grounds-aerial{top:926px;background:linear-gradient(180deg,#d9e6ec 0,#3f7a25 12%,#6c9a3a 55%,#2f5a1c 100%)}
  .intro{
    position:absolute;right:39px;top:540px;width:500px;text-align:right;
    font-family:"Cormorant Garamond",serif;font-style:italic;font-weight:500;font-size:17px;line-height:26.9px;color:var(--ink);
  }
  .intro span{display:block;white-space:nowrap}
  .divider{position:absolute;left:385px;top:786px;width:415px;height:1.5px;background:var(--orange)}
  .info-col{position:absolute;top:806px}
  .info-col.keywords{left:384px}
  .info-col.fees{left:614px}
  .info-col h2{
    font-family:"Montserrat",sans-serif;font-weight:600;font-size:20.5px;color:var(--orange);margin-bottom:8px;
  }
  .info-col li{
    list-style:none;font-family:"Cutive",serif;font-size:13.5px;line-height:35px;color:var(--ink);white-space:nowrap;
  }
  .contact{
    position:absolute;right:37px;top:1055px;text-align:right;color:#fff;
    font-family:"Montserrat",sans-serif;
  }
  .contact .label{font-weight:600;font-size:22px;line-height:30px}
  .contact .phone{display:flex;align-items:center;justify-content:flex-end;gap:12px;font-family:"Cutive",serif;font-size:28px;margin-top:8px}
  .contact svg{width:36px;height:36px}
</style>
</head>
<body>
<main class="flyer">
  <svg class="flyer-art" viewBox="0 0 836 1183" xmlns="http://www.w3.org/2000/svg">
    <defs>
      <linearGradient id="meadow" x1="0" y1="0" x2="1" y2="1">
        <stop offset="0" stop-color="var(--meadow-2)"/>
        <stop offset="0.5" stop-color="var(--meadow-1)"/>
        <stop offset="1" stop-color="var(--meadow-3)"/>
      </linearGradient>
    </defs>
    <path role="img" aria-label="Photo: a smiling woman in a straw hat hugging her dark horse in a green meadow"
      d="M0 150 C200 120 380 60 560 80 C680 92 770 100 836 95 L836 430 C700 440 560 500 420 540 C260 580 120 540 0 520 Z"
      fill="url(#meadow)"/>
    <path d="M0 0 H836 V95 C760 75 660 70 540 80 C380 95 200 190 0 215 Z" fill="var(--orange)"/>
    <path d="M0 185 C200 165 380 95 560 88 C680 82 770 95 836 110 V95 C760 75 660 70 540 80 C380 95 200 190 0 215 Z" fill="var(--orange-deep)"/>
    <path d="M280 180 C420 120 560 100 700 118 C760 126 810 140 836 150" stroke="var(--peach)" stroke-opacity="0.55" stroke-width="5" fill="none"/>
    <path d="M0 485 C120 520 250 545 400 520 C560 492 700 435 836 420 V470 C700 470 560 510 420 545 C260 580 120 570 0 545 Z" fill="var(--orange)"/>
    <path d="M0 430 C140 470 300 510 520 470" stroke="#fff" stroke-opacity="0.6" stroke-width="5" fill="none"/>
    <path d="M0 1085 C180 1150 420 1120 600 1020 C690 975 770 975 836 985 V1183 H0 Z" fill="var(--orange)"/>
    <path d="M0 1080 C200 1160 440 1140 620 1010 C460 1120 200 1140 0 1098 Z" fill="var(--orange-soft)"/>
  </svg>

  <h1 class="title">Willow Brook<br>at 34 Meadows</h1>

  <div class="facility-photo barn-aerial" role="img" aria-label="Aerial photo of the main barn and driveway among trees"></div>
  <div class="facility-photo stall-aisle" role="img" aria-label="Photo of the wooden stable aisle lined with stalls"></div>
  <div class="facility-photo grounds-aerial" role="img" aria-label="Aerial photo of the wooded grounds and riding arena"></div>

  <p class="intro">
    <span>Now available a premier retirement horse</span>
    <span>boarding facility, where luxury meets equestrian excellence!</span>
    <span>We have 6 available stalls, conveniently located in Cedar Hollow, TN. Our</span>
    <span>facility offers top tier amenities where every detail is meticulously crafted to</span>
    <span>ensure quality care for your retired equine companions.&nbsp; From spacious stalls</span>
    <span>with back patios to lush pastures for gentle exercise, every detail is crafted to</span>
    <span>ensure well being. You have access to a world class riding arena with stadium</span>
    <span>passionate , loving care from a staff with decades of experience.</span>
  </p>

  <div class="divider"></div>

  <section class="info-col keywords">
    <h2>Key Words:</h2>
    <ul>
      <li>Luxurious.</li>
      <li>Quality Facilities.</li>
      <li>Loving Care.</li>
      <li>Peaceful.&nbsp; Kind.</li>
    </ul>
  </section>

  <section class="info-col fees">
    <h2>Boarding Fees:</h2>
    <ul>
      <li>1st horse - $1,100/mo</li>
      <li>2nd horse - $900/mo</li>
      <li>3rd horse - $700/mo</li>
    </ul>
  </section>

  <div class="contact">
    <div class="label">Call / text Rosalind</div>
    <div class="phone">
      <svg viewBox="0 0 36 36" aria-hidden="true">
        <circle cx="18" cy="18" r="16" fill="none" stroke="#fff" stroke-width="2"/>
        <path d="M12.5 10.5 l3 -1 l2 4.5 l-2 1.5 c1 2.5 3 4.5 5.5 5.5 l1.5 -2 l4.5 2 l-1 3 c-7 1 -14.5 -6.5 -13.5 -13.5 z" fill="#fff"/>
      </svg>
      <span>555-014-2738</span>
    </div>
  </div>
</main>
</body>
</html>
```